R&t Subterra

We specialize in CIPP pipe lining but do other underground utilities trenchless as well.

Target Market(s)

Trenchless sewer replacement

Contact Information for Business Card

Gavin Holtby 715-482-6130 Pine Hollow, wi

```html
<!DOCTYPE html>
<html lang="en">
<head>
<meta charset="utf-8">
<title>R&amp;T Subterra – Business Card</title>
<link rel="stylesheet" href="https://fonts.googleapis.com/css2?family=Krona+One&family=Poppins:wght@500;600;700&display=swap">
<style>
  :root {
    --page-bg: #8a8a8c;
    --blue-deep: #2a7fc4;
    --blue-mid: #3592d2;
    --blue-light: #4aaee0;
    --blue-name: #2f7fc3;
    --blue-name-light: #4ba6e3;
    --grey-text: #8b8b8e;
    --white: #ffffff;
    --deco-grey: #ebebec;
    --deco-blue: #d6e3f4;
  }
  * { margin: 0; padding: 0; box-sizing: border-box; }
  html, body { width: 900px; height: 1200px; overflow: hidden; }
  body {
    background: var(--page-bg);
    position: relative;
    font-family: "Poppins", sans-serif;
  }
  .card {
    position: absolute;
    left: 135px;
    width: 630px;
    height: 358px;
    border-radius: 12px;
    overflow: hidden;
  }
  /* Front */
  .card-front { top: 215px; background: var(--blue-mid); }
  .front-pattern {
    position: absolute;
    inset: 0;
    background: linear-gradient(100deg, var(--blue-deep) 0%, var(--blue-mid) 55%, var(--blue-light) 100%);
  }
  .brand-row {
    position: absolute;
    left: 339px;
    top: 228px;
    display: flex;
    align-items: center;
    gap: 10px;
  }
  .brand-dot {
    width: 40px;
    height: 40px;
    border-radius: 50%;
    background: var(--white);
    flex: none;
  }
  .brand-name {
    font-family: "Poppins", sans-serif;
    font-weight: 700;
    font-size: 32px;
    color: var(--white);
    line-height: 1;
    white-space: nowrap;
  }
  /* Back */
  .card-back { top: 628px; background: var(--white); }
  .back-decoration {
    position: absolute;
    left: 390px;
    top: 12px;
    width: 340px;
    height: 340px;
    border-radius: 50%;
    background: radial-gradient(circle at 70% 55%, var(--deco-blue) 0%, var(--deco-blue) 45%, var(--deco-grey) 75%);
  }
  .back-brand {
    position: absolute;
    left: 36px;
    top: 52px;
    display: flex;
    align-items: center;
    gap: 10px;
  }
  .back-brand .brand-dot { background: var(--blue-name); }
  .back-brand .brand-name { color: var(--blue-name); }
  .holder-name {
    position: absolute;
    left: 142px;
    top: 186px;
    font-family: "Krona One", sans-serif;
    font-weight: 400;
    font-size: 30px;
    line-height: 30px;
    letter-spacing: 0.5px;
  }
  .holder-name .first { color: var(--blue-name); display: block; }
  .holder-name .last { color: var(--blue-name-light); display: block; }
  .contact {
    position: absolute;
    left: 142px;
    display: flex;
    align-items: center;
    gap: 8px;
    color: var(--grey-text);
    white-space: nowrap;
  }
  .contact-phone { top: 266px; font-weight: 700; font-size: 19px; letter-spacing: 5.5px; }
  .contact-place { top: 299px; font-weight: 600; font-size: 18px; }
  .contact svg { flex: none; }
</style>
</head>
<body>
  <section class="card card-front">
    <div class="front-pattern" role="img" aria-label="Repeating pattern of the company emblem on blue"></div>
    <div class="brand-row">
      <span class="brand-dot"></span>
      <span class="brand-name">R&amp;T Subterra</span>
    </div>
  </section>

  <section class="card card-back">
    <div class="back-decoration" role="img" aria-label="Large faint company emblem as background decoration"></div>
    <div class="back-brand">
      <span class="brand-dot"></span>
      <span class="brand-name">R&amp;T Subterra</span>
    </div>
    <h1 class="holder-name">
      <span class="first">GAVIN</span>
      <span class="last">HOLTBY</span>
    </h1>
    <p class="contact contact-phone">
      <svg width="18" height="18" viewBox="0 0 24 24" aria-hidden="true"><path fill="#2f7fc3" d="M6.6 10.8c1.4 2.8 3.8 5.1 6.6 6.6l2.2-2.2c.3-.3.7-.4 1-.2 1.1.4 2.3.6 3.6.6.6 0 1 .4 1 1V20c0 .6-.4 1-1 1C10.6 21 3 13.4 3 4c0-.6.4-1 1-1h3.5c.6 0 1 .4 1 1 0 1.3.2 2.5.6 3.6.1.3 0 .7-.2 1z"/></svg>
      715-482-6130
    </p>
    <p class="contact contact-place">
      <svg width="18" height="22" viewBox="0 0 24 30" aria-hidden="true"><path fill="#4ba6e3" d="M12 0C5.9 0 1 4.9 1 11c0 8 11 19 11 19s11-11 11-19C23 4.9 18.1 0 12 0zm0 15a4 4 0 1 1 0-8 4 4 0 0 1 0 8z"/></svg>
      Pine Hollow, wi
    </p>
  </section>
</body>
</html>
```